website design Investment Fund

I am looking for a custom website that will work on desktop computer, tablet device and a cellular device. I have attached the booklet so you can get an idea of the look we are going for. Would like to use the website eventually for crowdfunding. We like the ski racer and mountain climbing designs.

Target Market(s)

Financial Services

Industry/Entity Type

Financial Service

Coding

Coded - Design and coding required

Number of Pages Required

5+ page

Font styles to use
Sans Serif

Requirements
Must have
• Must be viewable on a cell phone and tablet and desktop
Nice to have
• Contact us form

```html
<!DOCTYPE html>
<html lang="en">
<head>
<meta charset="utf-8">
<title>Summit Ridge Capital — Desktop and Mobile Layouts</title>
<link href="https://fonts.googleapis.com/css2?family=Montserrat:wght@500;600;700;800&family=Open+Sans:wght@400;600&display=swap" rel="stylesheet">
<style>
:root{
  --blue:#1c4ea6;
  --blue-dark:#163f8a;
  --red:#e5262c;
  --ink:#1f2227;
  --text:#555a62;
  --muted:#9aa0a8;
  --ghost:#edeff2;
  --grey-bg:#eef0f3;
  --page:#dfe3e8;
  --white:#ffffff;
  --footer:#3c3f44;
}
*{box-sizing:border-box;margin:0;padding:0}
html,body{width:1200px;height:3478px;overflow:hidden}
body{background:var(--page);font-family:"Open Sans",Arial,sans-serif;color:var(--text);position:relative}
h1,h2,h3,h4,.brand,.btn,.nav,.phones{font-family:"Montserrat",Arial,sans-serif}

/* ---------- shared ---------- */
.photo{display:block}
.btn{display:inline-block;background:var(--red);color:var(--white);font-weight:700;letter-spacing:.5px;text-transform:uppercase}
.btn::after{content:" \203A"}
.btn-outline{background:none;border:1.5px solid var(--white);border-radius:20px}
.btn-outline::after{content:""}
.ribbon{display:inline-block;background:var(--blue);color:var(--white);font-family:"Montserrat",Arial,sans-serif;font-weight:700;letter-spacing:2px;text-transform:uppercase}
.torn{position:absolute;left:0;bottom:-1px;width:100%}
.section-title{position:relative;text-align:center}
.section-title .ghost{position:absolute;left:0;right:0;font-family:"Montserrat",Arial,sans-serif;font-weight:800;color:var(--ghost);letter-spacing:2px;white-space:nowrap}
.section-title h2{position:relative;color:var(--ink);font-weight:700;letter-spacing:.5px}
.section-title p{position:relative;color:var(--muted)}
.grey{background:var(--grey-bg)}
.hex{clip-path:polygon(50% 0,100% 25%,100% 75%,50% 100%,0 75%,0 25%)}
.stat{display:flex;align-items:center;font-family:"Montserrat",Arial,sans-serif;font-weight:700;color:var(--ink);text-transform:uppercase}
.stat-icon{border:1.5px solid var(--blue);display:flex;align-items:center;justify-content:center;flex:none}

/* ---------- desktop ---------- */
.desktop{position:absolute;left:28px;top:40px;width:800px;background:var(--white);box-shadow:0 10px 30px rgba(0,0,0,.15)}
.d-hero{position:relative;height:320px;background:linear-gradient(180deg,#4e6a94 0%,#8ea6c4 45%,#c9d6e4 75%,#eef2f6 100%)}
.d-hero .photo{position:absolute;inset:0}
.d-header{position:relative;display:flex;justify-content:space-between;padding:10px 150px 0 150px}
.brand{display:flex;align-items:center;gap:6px;color:var(--white);font-weight:700;text-transform:uppercase;line-height:1.1}
.brand-mark{background:var(--red);flex:none}
.d-brand{margin-top:22px;font-size:9px}
.d-brand .brand-mark{width:12px;height:12px}
.brand small{display:block;font-size:.7em;font-weight:500;letter-spacing:.5px}
.phones{display:flex;gap:14px;align-items:flex-start;color:var(--white)}
.phones b{display:block;font-size:8px}
.phones span{display:block;font-size:5px;opacity:.85}
.d-header .btn{font-size:6px;padding:4px 8px;border-radius:2px}
.nav{display:flex;gap:20px;margin-top:14px;font-size:6.5px;color:var(--white);text-transform:uppercase;font-weight:600}
.nav .active{border-bottom:1px solid var(--white);padding-bottom:3px}
.d-hero-copy{position:absolute;left:0;right:0;top:150px;text-align:center}
.headline{position:relative;display:inline-block;color:var(--white);font-weight:700;text-transform:uppercase;line-height:1.15}
.d-hero-copy .headline{font-size:24px;padding:0 30px}
.headline::before,.headline::after{content:"";position:absolute;width:24px;height:36px;border:1px solid rgba(255,255,255,.8)}
.headline::before{left:0;top:8px;border-right:0;border-bottom:0}
.headline::after{right:0;top:8px;border-left:0;border-bottom:0}
.d-hero-copy .ribbon{display:block;width:max-content;margin:4px auto 0;font-size:8px;padding:3px 8px}
.d-hero-copy .btn{margin-top:20px;font-size:5.5px;padding:6px 10px;border-radius:2px}

.d-about{padding:40px 0 36px}
.d-about .ghost{top:-12px;font-size:58px}
.d-about h2{font-size:14px;padding-top:22px}
.d-about .section-title p{font-size:7px;margin-top:10px}
.d-about-row{display:flex;gap:12px;width:510px;margin:34px auto 0}
.d-about-row .photo{flex:none;width:195px;height:195px;background:linear-gradient(120deg,#8a6a52,#c49a7a 50%,#6d5644)}
.d-about-body{flex:1;min-width:0}
.d-about-body h3{color:var(--blue);font-size:7.5px;margin-bottom:8px}
.d-about-body p{font-size:5.2px;line-height:1.6;margin-bottom:6px}
.d-stats{display:flex;gap:14px;margin:10px 0}
.d-stats .stat{font-size:5px;gap:6px}
.d-stats .stat-icon{width:19px;height:19px}
.d-about-body .btn{font-size:6px;padding:4px 8px;border-radius:2px}

.d-boutique{position:relative;padding:26px 0 40px}
.d-feature{display:flex;align-items:center;gap:28px;width:380px;margin:0 auto}
.d-feature .hex{width:78px;height:88px;flex:none}
.d-feature h3{color:var(--blue);font-size:8px;line-height:1.2;text-transform:uppercase;margin-bottom:5px}
.d-feature p{font-size:4.8px;line-height:1.7}
.d-feature + .d-feature{margin-top:16px}
.dots{color:var(--muted);font-size:8px;letter-spacing:1px;flex:none}

.d-invest{position:relative;padding:40px 0 34px}
.d-invest .ghost{top:-6px;font-size:58px}
.d-invest h2{font-size:13px;padding-top:22px}
.d-invest .section-title p{font-size:6.5px;margin-top:12px}
.cards{display:flex;width:330px;margin:22px auto 0}
.card{flex:1;color:var(--white)}
.card .photo{height:102px}
.card-blue{background:var(--blue)}
.card-red{background:var(--red)}
.card-body{padding:12px 13px 18px;font-family:"Montserrat",Arial,sans-serif;text-transform:uppercase}
.card h4{font-size:6.5px;line-height:1.3}
.card .tag{display:inline-block;font-size:6px;font-weight:600;padding:3px 6px;margin:5px 0 12px}
.card-blue .tag{background:var(--red)}
.card-red .tag{background:var(--blue)}
.card .rate{font-size:6.5px;font-weight:700}
.card .rate-line{font-size:6px;font-weight:600;margin-top:2px}
.card .term{font-size:6px;text-transform:none;margin-top:2px}
.card .btn-outline{font-size:5px;padding:4px 10px;margin-top:14px}

.d-team{position:relative;padding:34px 0 44px}
.d-team .ghost{top:-8px;font-size:58px;color:#e2e5ea}
.d-team h2{font-size:14px;padding-top:22px}
.d-team .section-title p{font-size:6.5px;margin-top:12px}
.team{display:flex;gap:0;width:480px;margin:26px auto 0}
.member{flex:1;text-align:center;border-bottom:1px solid #dadde2;padding-bottom:10px}
.member .photo{height:142px;margin:0 2px;background:linear-gradient(180deg,#dfe3e8,#b9c0c9)}
.member h4{font-size:5.2px;color:var(--ink);margin-top:14px;text-transform:uppercase}
.member p{font-size:4.5px;color:var(--muted);margin-top:2px}

.d-contact{position:relative;padding:40px 0 36px}
.d-contact .ghost{top:-8px;font-size:58px}
.d-contact h2{font-size:14px;padding-top:22px}
.d-contact .section-title p{font-size:6.5px;margin-top:12px}
.form{width:238px;margin:22px auto 0;text-align:center}
.field{height:17px;border:1px solid #d8dbe0;margin-bottom:9px;font-size:5px;color:var(--muted);text-align:left;padding:5px 7px}
.field.area{height:70px}
.form .btn{font-size:5.5px;padding:5px 12px;margin-top:10px;border-radius:2px}

.d-footer{position:relative;background:linear-gradient(180deg,#f2f3f5 0%,#8d9196 30%,var(--footer) 55%);padding:40px 0 18px;color:#c9ccd1}
.d-footer .brand{justify-content:center;color:var(--blue);font-size:9px}
.d-footer .brand small{color:var(--blue)}
.d-footer .brand-mark{width:12px;height:12px}
.newsletter{display:flex;justify-content:space-between;align-items:center;width:470px;margin:44px auto 0}
.newsletter h4{color:var(--white);font-size:8px;text-transform:uppercase}
.newsletter p{font-size:5px}
.subscribe{display:flex}
.subscribe .input{width:150px;height:22px;background:#2c2f33;font-size:5px;padding:8px}
.subscribe .btn{font-size:5.5px;padding:8px 12px}
.subscribe .btn::after{content:""}
.footer-cols{display:flex;gap:24px;width:470px;margin:40px auto 0}
.footer-cols h5{font-family:"Montserrat",Arial,sans-serif;font-size:6px;color:var(--white);text-transform:uppercase;margin-bottom:8px}
.footer-cols p,.footer-cols li{font-size:4.8px;line-height:1.7;list-style:none}
.col-about{width:150px}
.col-links{width:70px}
.col-contact{width:110px}
.col-phone b{display:block;color:var(--white);font-size:6.5px;font-family:"Montserrat",Arial,sans-serif}
.col-phone span{display:block;font-size:4px;margin-bottom:3px}
.copyright{display:flex;justify-content:space-between;width:470px;margin:34px auto 0;font-size:4.5px}
.social{display:flex;gap:6px}
.social i{width:6px;height:6px;border-radius:50%;background:#9aa0a8;display:block}

/* ---------- mobile ---------- */
.mobile{position:absolute;left:858px;top:40px;width:314px;height:3130px;overflow:hidden;background:var(--white);box-shadow:0 10px 30px rgba(0,0,0,.15)}
.m-hero{position:relative;height:585px}
.m-hero .photo{position:absolute;inset:0;background:linear-gradient(180deg,#3f5d8a 0%,#7e98bb 40%,#b8c8dc 75%,#edf1f5 100%)}
.m-menu{position:absolute;right:14px;top:14px;width:34px;height:30px;background:var(--blue);display:flex;flex-direction:column;justify-content:center;align-items:center;gap:4px}
.m-menu i{display:block;width:14px;height:1.5px;background:var(--white)}
.m-brand{position:absolute;top:40px;left:0;right:0;flex-direction:column;text-align:center;font-size:14px;gap:8px}
.m-brand .brand-mark{width:22px;height:22px}
.m-hero-copy{position:absolute;left:0;right:0;top:315px;text-align:center}
.m-hero-copy .headline{font-size:19px;padding:0 26px}
.m-hero-copy .ribbon{display:block;width:max-content;margin:4px auto 0;font-size:10px;padding:4px 10px}
.m-hero-copy .btn{margin-top:22px;font-size:9px;padding:9px 16px;border-radius:2px}

.m-about{padding:46px 15px 40px}
.m-about .ghost{top:-14px;font-size:44px}
.m-about h2{font-size:19px}
.m-about .section-title p{font-size:12px;margin-top:14px}
.m-about .photo{height:290px;margin-top:20px;background:linear-gradient(120deg,#8a6a52,#c49a7a 50%,#6d5644)}
.m-about h3{color:var(--blue);font-size:12px;margin:28px 0 14px}
.m-about p.body{font-size:9.2px;line-height:1.75;margin-bottom:14px}
.m-stats .stat{font-size:9px;gap:12px;margin-top:12px;line-height:1.4}
.m-stats .stat-icon{width:36px;height:36px}
.m-about .btn{font-size:10px;padding:8px 13px;margin-top:24px}

.m-boutique{padding:44px 18px 50px;text-align:center}
.m-boutique .hex{width:138px;height:150px;margin:0 auto}
.m-boutique .dots{display:block;margin:8px 0 10px}
.m-boutique h3{color:var(--blue);font-size:15px;line-height:1.2;text-transform:uppercase;margin-bottom:14px}
.m-boutique p{font-size:9px;line-height:2.1}
.m-boutique .block + .block{margin-top:40px}

.m-invest{padding:40px 12px 0}
.m-invest .ghost{top:-16px;font-size:40px}
.m-invest h2{font-size:16px}
.m-invest .section-title p{font-size:12px;margin-top:10px}
.m-card{margin-top:26px;color:var(--white);background:var(--blue)}
.m-card .photo{height:166px}
.m-card .card-body{padding:26px 22px 30px}
.m-card h4{font-size:12px;line-height:1.3}
.m-card .tag{display:inline-block;background:var(--red);font-size:11.5px;font-weight:600;padding:6px 10px;margin:10px 0 26px}
.m-card .rate{font-size:12px;font-weight:700}
.m-card .rate-line{font-size:11px;font-weight:600;margin-top:6px}
.m-card .term{font-size:11px;text-transform:none;margin-top:6px}
.m-card .btn-outline{font-size:9.5px;padding:7px 15px;margin-top:24px}
.m-photo-next{height:80px;margin-top:24px}

.snow{background:linear-gradient(180deg,#5a86c9 0%,#a9c4e6 45%,#f1f4f8 100%)}
.snow-field{background:linear-gradient(180deg,#9bb3cf 0%,#dfe6ee 55%,#b3a999 100%)}
.climber{background:linear-gradient(135deg,#f2b45a 0%,#d97a34 40%,#4a5566 100%)}
.peak{background:linear-gradient(180deg,#6f8fbd 0%,#dfe8f2 55%,#8a96a4 100%)}
</style>
</head>
<body>

<main class="desktop">

  <section class="d-hero">
    <div class="photo" role="img" aria-label="Skier racing down a snowy mountain slope"></div>
    <header class="d-header">
      <div class="brand d-brand"><span class="brand-mark"></span><div>Summit Ridge Capital<small>Management, LLC</small></div></div>
      <div>
        <div class="phones">
          <div><b>480-555-0141</b><span>Daniel R. Hale</span></div>
          <div><b>480-555-0172</b><span>Peter Vance</span></div>
          <div><b>602-555-0125</b><span>Laura Benning</span></div>
          <div><b>602-555-0190</b><span>Samuel Grant</span></div>
          <span class="btn">Contact Us</span>
        </div>
        <nav class="nav"><span class="active">Home</span><span>Objective</span><span>Services</span><span>Clients</span><span>Loan Programs</span><span>Team</span><span>Contact</span></nav>
      </div>
    </header>
    <div class="d-hero-copy">
      <h1 class="headline">Your Elite Boutique<br>Lender</h1>
      <span class="ribbon">Where Creativity Counts</span>
      <br><span class="btn">Get Free Consultation</span>
    </div>
    <svg class="torn" viewBox="0 0 800 14" preserveAspectRatio="none" height="14"><polygon fill="#fff" points="0,14 0,6 12,9 22,4 34,8 46,3 58,7 70,2 84,8 96,5 110,9 122,3 136,7 150,4 164,9 176,5 190,8 204,2 218,7 232,4 246,9 260,5 274,8 288,3 302,7 316,4 330,9 344,5 358,8 372,2 386,7 400,4 414,9 428,5 442,8 456,3 470,7 484,4 498,9 512,5 526,8 540,2 554,7 568,4 582,9 596,5 610,8 624,3 638,7 652,4 666,9 680,5 694,8 708,2 722,7 736,4 750,9 764,5 778,8 790,4 800,7 800,14"/></svg>
  </section>

  <section class="d-about">
    <div class="section-title">
      <span class="ghost">ABOUT US</span>
      <h2>THE COMPANY</h2>
      <p>Arizona's Elite Boutique Lender</p>
    </div>
    <div class="d-about-row">
      <div class="photo" role="img" aria-label="Rock climber scaling a cliff face"></div>
      <div class="d-about-body">
        <h3>About Summit Ridge Capital</h3>
        <p>Ridgeline Funding &amp; Investment, Inc. is a privately held mortgage lender, asset management and advisory firm headquartered in Cedar Heights, Arizona which specializes in fast financing for debt, equity, mezzanine and land bank on real estate projects in the $100,000 to $50,000,000 range. As a highly reputable, successful and growth-focused company with decades of experience across the entire spectrum of real estate financing through Arizona, the Southwest United States and Mexico.</p>
        <p>At Ridgeline, we've created an exceptional business focused on delivering privately funded financing to a wide range of clients. Our proven diligence, impeccable operating standards and expertise help to ensure that the funding process will run more rapidly and reliably than any other company in that market.</p>
        <div class="d-stats">
          <div class="stat"><span class="stat-icon"><svg width="10" height="10" viewBox="0 0 10 10"><circle cx="5" cy="4" r="2" fill="none" stroke="#1c4ea6"/><path d="M1 10c0-3 8-3 8 0" fill="none" stroke="#1c4ea6"/></svg></span>37 Years of Entrepreneurial<br>Experiences</div>
          <div class="stat"><span class="stat-icon"><svg width="10" height="10" viewBox="0 0 10 10"><path d="M1 4L5 1l4 3M2 4v5M5 4v5M8 4v5M1 9.5h8" fill="none" stroke="#1c4ea6"/></svg></span>23 Years in the<br>Private Lender Business</div>
        </div>
        <span class="btn">Read More</span>
      </div>
    </div>
  </section>

  <section class="d-boutique grey">
    <div class="d-feature">
      <div class="hex climber" role="img" aria-label="Hiker with backpack on a summit at sunset"></div>
      <span class="dots">• • •</span>
      <div>
        <h3>The Boutique Fund<br>Investors Are Looking For</h3>
        <p>As an ELITE BOUTIQUE, full-service, and highly selective firm, we only present our investors deals with highly qualified borrowers and properties with loan to value ratios (LTV) not to exceed 65%-70%. Simply put, we only fund deals with enough equity to allow for a Real Estate market change. All loans are short term so we can easily monitor changes in valuation and market conditions.</p>
      </div>
    </div>
    <div class="d-feature">
      <div>
        <h3>Investment Strategy</h3>
        <p>The Fund Managers have decades of experience in private money lending as well as real estate investment, property and asset management, construction, and development. In order to produce the desired investor yields, the Fund Managers will utilize their extensive relationships in the marketplace to make a diversified series of investments in secured loans, equity joint ventures, and select value-add real estate investments.</p>
      </div>
      <span class="dots">• • •</span>
      <div class="hex peak" role="img" aria-label="Climber standing before snowy mountain peaks"></div>
    </div>
    <svg class="torn" viewBox="0 0 800 10" preserveAspectRatio="none" height="10"><polygon fill="#fff" points="0,10 0,5 20,7 40,3 60,6 80,2 100,6 120,3 140,7 160,4 180,6 200,2 220,6 240,3 260,7 280,4 300,6 320,2 340,6 360,3 380,7 400,4 420,6 440,2 460,6 480,3 500,7 520,4 540,6 560,2 580,6 600,3 620,7 640,4 660,6 680,2 700,6 720,3 740,7 760,4 780,6 800,3 800,10"/></svg>
  </section>

  <section class="d-invest">
    <div class="section-title">
      <span class="ghost">INVESTMENT</span>
      <h2>ACCREDITED INVESTORS ONLY</h2>
      <p>Minimum Investment Requirements</p>
    </div>
    <div class="cards">
      <article class="card card-blue">
        <div class="photo snow" role="img" aria-label="Skier carving through fresh snow"></div>
        <div class="card-body">
          <h4>Minimum Investment<br>Requirements</h4>
          <span class="tag">Series A $50,000-$249,999</span>
          <p class="rate">Rate of Return</p>
          <p class="rate-line">Series A 7% per annum</p>
          <p class="term">Term 24 Months</p>
          <span class="btn btn-outline">Learn More</span>
        </div>
      </article>
      <article class="card card-red">
        <div class="photo snow-field" role="img" aria-label="Mountaineer hiking across a rocky ridge"></div>
        <div class="card-body">
          <h4>Minimum Investment<br>Requirements</h4>
          <span class="tag">Series B $250,000.00</span>
          <p class="rate">Rate of Return</p>
          <p class="rate-line">Series B 8% per annum</p>
          <p class="term">Term 24 Months</p>
          <span class="btn btn-outline">Learn More</span>
        </div>
      </article>
    </div>
  </section>

  <section class="d-team grey">
    <div class="section-title">
      <span class="ghost">OUR TEAM</span>
      <h2>MEET OUR TEAM</h2>
      <p>Founding Members and Fund Managers</p>
    </div>
    <div class="team">
      <div class="member"><div class="photo" role="img" aria-label="Portrait of founder Daniel R. Hale"></div><h4>Daniel R. Hale</h4><p>Founder and Fund Manager</p></div>
      <div class="member"><div class="photo" role="img" aria-label="Portrait of Laura Benning"></div><h4>Laura Benning</h4><p>Founder and Managing Partner</p></div>
      <div class="member"><div class="photo" role="img" aria-label="Portrait of Peter Vance"></div><h4>Peter Vance</h4><p>Fund Advisor</p></div>
      <div class="member"><div class="photo" role="img" aria-label="Portrait of Samuel Grant"></div><h4>Samuel Grant</h4><p>Chief Investment Officer</p></div>
    </div>
    <svg class="torn" viewBox="0 0 800 10" preserveAspectRatio="none" height="10"><polygon fill="#fff" points="0,10 0,5 20,7 40,3 60,6 80,2 100,6 120,3 140,7 160,4 180,6 200,2 220,6 240,3 260,7 280,4 300,6 320,2 340,6 360,3 380,7 400,4 420,6 440,2 460,6 480,3 500,7 520,4 540,6 560,2 580,6 600,3 620,7 640,4 660,6 680,2 700,6 720,3 740,7 760,4 780,6 800,3 800,10"/></svg>
  </section>

  <section class="d-contact">
    <div class="section-title">
      <span class="ghost">CONTACT</span>
      <h2>KEEP IN TOUCH</h2>
      <p>Summit Ridge Capital Management, LLC</p>
    </div>
    <div class="form">
      <div class="field">Name</div>
      <div class="field">Email</div>
      <div class="field">Subject</div>
      <div class="field area">Message</div>
      <span class="btn">Submit</span>
    </div>
  </section>

  <footer class="d-footer">
    <div class="brand"><span class="brand-mark"></span><div>Summit Ridge Capital<small>Management, LLC</small></div></div>
    <div class="newsletter">
      <div><h4>Subscribe Our Newsletter</h4><p>Subscribe to our newsletter. Be informed about all our news</p></div>
      <div class="subscribe"><span class="input">Your email address</span><span class="btn">Subscribe</span></div>
    </div>
    <div class="footer-cols">
      <div class="col-about"><h5>About Us</h5><p>Ridgeline Funding &amp; Investment, Inc. is a privately held mortgage lender, asset management and advisory firm headquartered in Cedar Heights, Arizona which specializes in fast financing for debt, equity, mezzanine and land bank on real estate projects in the $100,000 to $50,000,000 range.</p><p>Read More</p></div>
      <div class="col-links"><h5>Useful Links</h5><ul><li>› Home</li><li>› About Us</li><li>› Objective</li><li>› Services</li><li>› Team</li><li>› Contact</li></ul></div>
      <div class="col-contact"><h5>Contact Us</h5><p>Address<br>2200 N. Canyon View Rd<br>Suite 8 Cedar Heights, AZ 85099</p><p>Email<br>info@summitridgecap.com</p></div>
      <div class="col-phone"><h5>Phone</h5><b>480-555-0141</b><span>DANIEL R. HALE</span><b>480-555-0172</b><span>PETER VANCE</span><b>602-555-0125</b><span>LAURA BENNING</span><b>602-555-0190</b><span>SAMUEL GRANT</span></div>
    </div>
    <div class="copyright"><span>Copyright © 2019 Summit Ridge Capital. All rights reserved | Privacy Policy</span><span class="social"><i></i><i></i><i></i><i></i></span></div>
  </footer>
</main>

<main class="mobile">
  <section class="m-hero">
    <div class="photo" role="img" aria-label="Skier racing down a snowy mountain slope"></div>
    <span class="m-menu"><i></i><i></i><i></i></span>
    <div class="brand m-brand"><span class="brand-mark"></span><div>Summit Ridge Capital<small>Management, LLC</small></div></div>
    <div class="m-hero-copy">
      <h1 class="headline">Your Elite Boutique<br>Lender</h1>
      <span class="ribbon">Where Creativity Counts</span>
      <span class="btn">Get Free Consultation</span>
    </div>
    <svg class="torn" viewBox="0 0 314 14" preserveAspectRatio="none" height="14"><polygon fill="#fff" points="0,14 0,6 14,9 28,4 42,8 56,3 70,7 84,2 98,8 112,4 126,9 140,3 154,7 168,4 182,9 196,5 210,8 224,2 238,7 252,4 266,9 280,5 294,8 314,4 314,14"/></svg>
  </section>

  <section class="m-about">
    <div class="section-title">
      <span class="ghost">ABOUT US</span>
      <h2>THE COMPANY</h2>
      <p>Arizona's Elite Boutique Lender</p>
    </div>
    <div class="photo" role="img" aria-label="Rock climber scaling a cliff face"></div>
    <h3>About Summit Ridge Capital</h3>
    <p class="body">Ridgeline Funding &amp; Investment, Inc. is a privately held mortgage lender, asset management and advisory firm headquartered in Cedar Heights, Arizona which specializes in fast financing for debt, equity, mezzanine and land bank on real estate projects in the $100,000 to $50,000,000 range. As a highly reputable, successful and growth-focused company with decades of experience across the entire spectrum of real estate financing through Arizona, the Southwest United States and Mexico.</p>
    <p class="body">At Ridgeline, we've created an exceptional business focused on delivering privately funded financing to a wide range of clients. Our proven diligence, impeccable operating standards and expertise help to ensure that the funding process will run more rapidly and reliably than any other company in that market.</p>
    <div class="m-stats">
      <div class="stat"><span class="stat-icon"><svg width="16" height="16" viewBox="0 0 10 10"><circle cx="5" cy="4" r="2" fill="none" stroke="#1c4ea6" stroke-width=".7"/><path d="M1 10c0-3 8-3 8 0" fill="none" stroke="#1c4ea6" stroke-width=".7"/></svg></span>37 Years of Entrepreneurial<br>Experiences</div>
      <div class="stat"><span class="stat-icon"><svg width="16" height="16" viewBox="0 0 10 10"><path d="M1 4L5 1l4 3M2 4v5M5 4v5M8 4v5M1 9.5h8" fill="none" stroke="#1c4ea6" stroke-width=".7"/></svg></span>23 Years in the<br>Private Lender Business</div>
    </div>
    <span class="btn">Read More</span>
  </section>

  <section class="m-boutique grey">
    <div class="block">
      <div class="hex climber" role="img" aria-label="Hiker with backpack on a summit at sunset"></div>
      <span class="dots">• • •</span>
      <h3>The Boutique Fund<br>Investors Are Looking For</h3>
      <p>As an ELITE BOUTIQUE, full-service, and highly selective firm, we only present our investors deals with highly qualified borrowers and properties with loan to value ratios (LTV) not to exceed 65%-70%. Simply put, we only fund deals with enough equity to allow for a Real Estate market change. All loans are short term so we can easily monitor changes in valuation and market conditions.</p>
    </div>
    <div class="block">
      <div class="hex peak" role="img" aria-label="Climber standing before snowy mountain peaks"></div>
      <span class="dots">• • •</span>
      <h3>Investment Strategy</h3>
      <p>The Fund Managers have decades of experience in private money lending as well as real estate investment, property and asset management, construction, and development. In order to produce the desired investor yields, the Fund Managers will utilize their extensive relationships in the marketplace to make a diversified series of investments in secured loans, equity joint ventures, and select value-add real estate investments.</p>
    </div>
  </section>

  <section class="m-invest">
    <div class="section-title">
      <span class="ghost">INVESTMENT</span>
      <h2>ACCREDITED INVESTORS ONLY</h2>
      <p>Minimum Investment Requirements</p>
    </div>
    <article class="m-card">
      <div class="photo snow" role="img" aria-label="Skier carving through fresh snow"></div>
      <div class="card-body">
        <h4>Minimum Investment<br>Requirements</h4>
        <span class="tag">Series A $50,000-$249,999</span>
        <p class="rate">Rate of Return</p>
        <p class="rate-line">Series A 7% per annum</p>
        <p class="term">Term 24 Months</p>
        <span class="btn btn-outline">Learn More</span>
      </div>
    </article>
    <div class="photo snow-field m-photo-next" role="img" aria-label="Mountaineer hiking across a rocky ridge"></div>
  </section>
</main>

</body>
</html>
```